VarnoBud CBD Tincture packaging design

We are seeking a designer to create the label that will be printed on cardboard box packaging, which will carry our CBD tincture. We envision the box being white to resemble a clean look that stands out on shelves. Our logo (attached) uses shades of yellows and greens in the form of a fluid drop resembling half plant and half plant extract. The packaging will show that we only use clean (TRELK certified) hemp extract thats been extracted using the cleanest method of extraction; supercritical CO2. Our tincture uses a fractionated coconut oil to improve absorption for the consumer, increasing onset time and providing essential omega fatty acids. We take pride in our use of a clean product with a clean extraction. The tincture bottle itself holds 30ml of liquid and is a clear glass bottle. The cap for the tincture bottle is white and has a graduated glass stem that shows the measurements for how much liquid it holds (picture attached). We have not yet done the label that will stick on the tincture, but i image it will be a frosted white label with the VarnoBud logo and a few words describing the product. This project is for the cardboard box that will hold each individual tincture bottle.

BOX DIMENSIONS: 1.31" x 1.31" x 4.13" (LxWxH)

We will be releasing a new product (cbd capsules) in April, and we will reach out to the designer of this product as first option to create the design for the capsule packaging.

Target Market(s)

convenience stores, medical marijuana dispensaries, health stores

Font styles to use
Serif

Colors
ffffff
fbed22
ffc214
ffcf3e
acd136
9bcb3c

Requirements
Must have
• -VarnoBud company logo
-Made with full spectrum supercritical CO2 Hemp Extract
-Made from TRELK certified clean hemp
-Declaration of ingredients (fractionated coconut oil, CBD hemp extract)
-1200mg CBD Tincture
-Nt. Wt. 1FL OZ (30ml)
-These statements have not been evaluated by the Bureau of Remedy Oversight. BRO has not evaluated this product for safety or efficacy. This product is not intended to diagnose, treat, cure or prevent any disease.
-DO NOT REFRIGERATE. Keep at room temperature to preserve freshness. Store away from humidity, heat, and light. Warning: If pregnant, nursing or taking prescription drugs, consult your physician prior to use. Keep out of reach of children.
-Manufactured by VarnoBud CBD Co. 58 Corrow Bend Ln. Scarborough, ME 04091
-Batch ID:___________
-Expiration Date:____________
-Good Manufacturing Practice (GMP) Logo
-TRELK logo
Nice to have
• -Contains omega 3, 6 and essential fatty acids
-Graduated dropper for precise dosing
-40mg of CBD per dropper!
-Made in the USA
-No Pesticides
-No Solvents
-No Heavy Metals
-CO2 Extraction
-3rd Party Lab Tested

```html
<!DOCTYPE html>
<html lang="en">
<head>
<meta charset="utf-8">
<title>VarnoBud CBD Tincture Drop – Box Dieline</title>
<link rel="stylesheet" href="https://fonts.googleapis.com/css2?family=Fredoka:wght@500;600&family=Questrial&display=swap">
<style>
  :root {
    --green-deep: #1e9a5a;
    --green-mid: #5fa646;
    --green-light: #9bcb3c;
    --green-pale: #dcedcc;
    --gold: #ffc214;
    --gold-soft: #d9b25a;
    --cut-red: #e0242b;
    --ink: #2b2b2b;
    --white: #ffffff;
  }
  html, body {
    margin: 0; padding: 0;
    width: 1200px; height: 800px;
    overflow: hidden;
    background: var(--white);
    font-family: "Questrial", sans-serif;
    color: var(--ink);
  }
  .dieline {
    position: absolute;
    left: 301px; top: 12px;
    width: 1050px; height: 1335px;
    transform: scale(0.58);
    transform-origin: 0 0;
  }
  .cut-lines { position: absolute; left: 0; top: 0; z-index: 5; pointer-events: none; }

  .top-band {
    position: absolute; left: 67px; top: 280px;
    width: 980px; height: 35px;
    background: var(--green-light);
  }
  .bottom-band {
    position: absolute; left: 67px; top: 1005px;
    width: 980px; height: 50px;
    background: var(--green-deep);
    border-top: 3px solid var(--gold-soft);
  }

  .panel {
    position: absolute; top: 315px;
    width: 245px; height: 690px;
    overflow: hidden;
    text-align: center;
  }
  .leaf-wash {
    position: absolute; left: 0; top: 0; width: 100%; height: 200px;
    background: linear-gradient(180deg, var(--green-pale) 0%, #eef6e6 55%, var(--white) 100%);
  }

  .brand {
    position: relative;
    display: flex; flex-direction: column; align-items: center;
  }
  .brand-dot {
    width: 22px; height: 22px; border-radius: 50%;
    background: var(--gold);
  }
  .brand-name {
    font-family: "Questrial", sans-serif;
    color: var(--ink);
    margin-top: 6px;
    line-height: 1;
  }

  /* front panel */
  .front .brand { margin-top: 48px; }
  .front .brand-name { font-size: 22px; }
  .cbd-mark {
    position: relative;
    font-family: "Fredoka", sans-serif; font-weight: 600;
    color: var(--green-deep);
    font-size: 104px; line-height: 0.9;
    letter-spacing: -2px;
    margin-top: 6px;
  }
  .tincture-bar {
    position: relative;
    display: flex; align-items: center;
    margin: 6px 5px 0;
    height: 22px;
  }
  .tincture-bar .word-tincture {
    background: var(--green-mid); color: var(--white);
    font-size: 13px; letter-spacing: 8px;
    height: 22px; line-height: 22px;
    padding: 0 4px 0 14px;
  }
  .tincture-bar .word-drop {
    font-family: "Fredoka", sans-serif; font-weight: 500;
    color: var(--green-deep);
    font-size: 25px; letter-spacing: 1px;
    padding-left: 4px; line-height: 22px;
  }
  .extract-line {
    position: relative;
    font-size: 11px; line-height: 1.1;
    margin-top: 20px; text-transform: uppercase;
  }
  .potency-pill {
    position: relative;
    display: inline-block;
    margin-top: 10px;
    background: var(--green-mid); color: var(--white);
    font-family: "Fredoka", sans-serif; font-weight: 600;
    font-size: 35px; line-height: 52px;
    padding: 0 20px; border-radius: 28px;
  }
  .ingredients {
    position: relative;
    margin-top: 8px; line-height: 1.1;
  }
  .ingredients .oil { display: block; font-size: 17px; }
  .ingredients .extract { display: block; font-size: 22px; }
  .front-sweep { position: absolute; left: 0; bottom: 0; }
  .leaf-seal {
    position: absolute; left: 93px; top: 570px;
    width: 82px; height: 82px; border-radius: 50%;
    background: radial-gradient(circle, #e9f4dd 0%, #b9db92 100%);
    border: 5px solid var(--white);
    box-shadow: 0 0 0 3px var(--green-mid);
  }

  /* side panel */
  .side .brand { margin-top: 38px; }
  .side .brand-dot { width: 30px; height: 30px; }
  .side .brand-name { font-size: 34px; margin-top: 8px; }
  .disclaimer {
    position: relative;
    font-size: 8.4px; line-height: 1.2;
    margin: 10px 14px 0;
  }
  .claims {
    position: relative;
    list-style: none; text-align: left;
    margin: 10px 14px 0 14px; padding: 0 0 6px;
    background: var(--green-mid);
  }
  .claims li {
    color: var(--white);
    font-size: 8.6px; line-height: 17px;
    padding-left: 6px;
  }
  .claims li:first-child {
    background: var(--green-deep);
    margin-right: -14px; margin-left: 0;
  }
  .storage, .warning {
    position: relative;
    font-size: 10px; line-height: 1.2;
    margin: 16px 16px 0;
  }
  .storage .head, .warning .head { display: block; }
  .warning { margin-top: 12px; }
  .rule {
    position: relative;
    height: 3px; background: var(--green-mid);
    margin: 14px 26px 0;
  }
  .badges {
    position: relative;
    display: flex; justify-content: space-around;
    margin: 14px 30px 0;
  }
  .badge {
    width: 56px; height: 56px; border-radius: 50%;
    border: 3px solid var(--green-mid);
    background: var(--green-pale);
  }
  .maker {
    position: relative;
    text-align: left;
    font-size: 10px; line-height: 1.2;
    margin: 16px 10px 0;
  }
  .maker b { font-weight: normal; font-family: "Fredoka", sans-serif; font-weight: 500; }
  .side .footer-rule {
    position: absolute; left: 0; right: 0; bottom: 2px;
    height: 2px; background: var(--gold-soft);
  }

  .net-weight {
    position: absolute; top: 1015px;
    width: 245px; text-align: center;
    font-family: "Fredoka", sans-serif; font-weight: 600;
    color: var(--white); font-size: 19px;
    z-index: 3;
  }

  /* lid */
  .lid {
    position: absolute; left: 557px; top: 72px;
    width: 245px; height: 208px;
    overflow: hidden; text-align: center;
  }
  .lid-inner {
    position: absolute; inset: 0;
    transform: rotate(180deg);
  }
  .lid .leaf-wash { top: auto; bottom: 0; height: 150px;
    background: linear-gradient(0deg, var(--green-pale) 0%, var(--white) 100%); }
  .lid .brand { margin-top: 14px; }
  .lid .brand-name { font-size: 20px; }
  .lid .cbd-mark { font-size: 78px; margin-top: 4px; }
  .lid .tincture-bar { justify-content: center; margin-top: 2px; height: 16px; }
  .lid .tincture-bar .word-tincture { font-size: 10px; letter-spacing: 6px; height: 16px; line-height: 16px; }
  .lid .tincture-bar .word-drop { font-size: 18px; line-height: 16px; }
</style>
</head>
<body>
<main class="dieline" aria-label="VarnoBud CBD Tincture Drop carton, flat dieline">

  <div class="top-band"></div>

  <!-- front panel A -->
  <section class="panel front" style="left:67px">
    <div class="leaf-wash" role="img" aria-label="Faint hemp leaf pattern"></div>
    <div class="brand"><span class="brand-dot"></span><span class="brand-name">VarnoBud</span></div>
    <div class="cbd-mark">CBD</div>
    <div class="tincture-bar"><span class="word-tincture">TINCTURE</span><span class="word-drop">DROP</span></div>
    <p class="extract-line">Full spectrum supercritical CO2<br>hemp extract</p>
    <div class="potency-pill">1200MG</div>
    <p class="ingredients"><span class="oil">Fractionated Coconut Oil,</span><span class="extract">CBD Hemp Extract</span></p>
    <svg class="front-sweep" width="245" height="140" viewBox="0 0 245 140" aria-hidden="true">
      <polygon points="0,140 245,5 245,140" fill="#1e9a5a"/>
      <line x1="0" y1="138" x2="245" y2="3" stroke="#d9b25a" stroke-width="3"/>
    </svg>
    <div class="leaf-seal" role="img" aria-label="Hemp leaf seal"></div>
  </section>

  <!-- side panel B -->
  <section class="panel side" style="left:312px">
    <div class="leaf-wash" role="img" aria-label="Faint hemp leaf pattern"></div>
    <div class="brand"><span class="brand-dot"></span><span class="brand-name">VarnoBud</span></div>
    <p class="disclaimer">These statements have not been evaluated by the Bureau of Remedy Oversight. BRO has not evaluated this product for safety or efficacy. This product is not intended to diagnose, treat, cure or prevent any disease.</p>
    <ul class="claims">
      <li>- Contains omega 3, 6 and essential fatty acids</li>
      <li>- Graduated dropper for precise dosing</li>
      <li>- 40mg of CBD per dropper!</li>
      <li>- Made in the USA</li>
      <li>- No Pesticides</li>
      <li>- No Solvents</li>
      <li>- No Heavy Metals</li>
      <li>- CO2 Extraction</li>
      <li>- 3rd Party Lab Tested</li>
    </ul>
    <p class="storage"><span class="head">-DO NOT REFRIGERATE-</span>Keep at room temperature to preserve freshness. Store away from humidity, heat, and light.</p>
    <p class="warning"><span class="head">Warning</span>If pregnant, nursing or taking prescription drugs, consult your physician prior to use. Keep out of reach of children.</p>
    <div class="rule"></div>
    <div class="badges">
      <span class="badge" role="img" aria-label="TRELK certified badge"></span>
      <span class="badge" role="img" aria-label="GMP certified badge"></span>
    </div>
    <p class="maker"><b>Manufactured by<br>VarnoBud CBD Co.</b><br>58 Corrow Bend Ln.<br>Scarborough, ME 04091<br><b>Batch ID:</b>___________<br><b>Expiration Date:</b>____________</p>
    <div class="footer-rule"></div>
  </section>

  <!-- front panel C -->
  <section class="panel front" style="left:557px">
    <div class="leaf-wash" role="img" aria-label="Faint hemp leaf pattern"></div>
    <div class="brand"><span class="brand-dot"></span><span class="brand-name">VarnoBud</span></div>
    <div class="cbd-mark">CBD</div>
    <div class="tincture-bar"><span class="word-tincture">TINCTURE</span><span class="word-drop">DROP</span></div>
    <p class="extract-line">Full spectrum supercritical CO2<br>hemp extract</p>
    <div class="potency-pill">1200MG</div>
    <p class="ingredients"><span class="oil">Fractionated Coconut Oil,</span><span class="extract">CBD Hemp Extract</span></p>
    <svg class="front-sweep" width="245" height="140" viewBox="0 0 245 140" aria-hidden="true">
      <polygon points="0,140 245,5 245,140" fill="#1e9a5a"/>
      <line x1="0" y1="138" x2="245" y2="3" stroke="#d9b25a" stroke-width="3"/>
    </svg>
    <div class="leaf-seal" role="img" aria-label="Hemp leaf seal"></div>
  </section>

  <!-- side panel D -->
  <section class="panel side" style="left:802px">
    <div class="leaf-wash" role="img" aria-label="Faint hemp leaf pattern"></div>
    <div class="brand"><span class="brand-dot"></span><span class="brand-name">VarnoBud</span></div>
    <p class="disclaimer">These statements have not been evaluated by the Bureau of Remedy Oversight. BRO has not evaluated this product for safety or efficacy. This product is not intended to diagnose, treat, cure or prevent any disease.</p>
    <ul class="claims">
      <li>- Contains omega 3, 6 and essential fatty acids</li>
      <li>- Graduated dropper for precise dosing</li>
      <li>- 40mg of CBD per dropper!</li>
      <li>- Made in the USA</li>
      <li>- No Pesticides</li>
      <li>- No Solvents</li>
      <li>- No Heavy Metals</li>
      <li>- CO2 Extraction</li>
      <li>- 3rd Party Lab Tested</li>
    </ul>
    <p class="storage"><span class="head">-DO NOT REFRIGERATE-</span>Keep at room temperature to preserve freshness. Store away from humidity, heat, and light.</p>
    <p class="warning"><span class="head">Warning</span>If pregnant, nursing or taking prescription drugs, consult your physician prior to use. Keep out of reach of children.</p>
    <div class="rule"></div>
    <div class="badges">
      <span class="badge" role="img" aria-label="TRELK certified badge"></span>
      <span class="badge" role="img" aria-label="GMP certified badge"></span>
    </div>
    <p class="maker"><b>Manufactured by<br>VarnoBud CBD Co.</b><br>58 Corrow Bend Ln.<br>Scarborough, ME 04091<br><b>Batch ID:</b>___________<br><b>Expiration Date:</b>____________</p>
    <div class="footer-rule"></div>
  </section>

  <div class="bottom-band"></div>
  <div class="net-weight" style="left:67px">Nt. Wt. 1FL OZ (30ml)</div>
  <div class="net-weight" style="left:557px">Nt. Wt. 1FL OZ (30ml)</div>

  <!-- top tuck lid, printed upside down -->
  <section class="lid">
    <div class="lid-inner">
      <div class="leaf-wash" role="img" aria-label="Faint hemp leaf pattern"></div>
      <div class="brand"><span class="brand-dot"></span><span class="brand-name">VarnoBud</span></div>
      <div class="cbd-mark">CBD</div>
      <div class="tincture-bar"><span class="word-tincture">TINCTURE</span><span class="word-drop">DROP</span></div>
    </div>
  </section>

  <svg class="cut-lines" width="1050" height="1335" viewBox="0 0 1050 1335" fill="none" stroke="#e0242b" stroke-width="3" aria-hidden="true">
    <!-- glue flap -->
    <path d="M67,280 L0,315 V1020 L67,1055"/>
    <!-- body -->
    <rect x="67" y="280" width="980" height="775"/>
    <!-- top dust flaps -->
    <path d="M312,280 V268 L325,258 V210 Q325,185 350,185 H512 Q537,185 537,210 V265 L557,280"/>
    <path d="M802,280 L822,265 V210 Q822,185 847,185 H1010 Q1035,185 1035,210 V258 L1047,268 V280"/>
    <!-- top tuck lid -->
    <path d="M557,280 V76 L567,68 V48 Q567,0 615,0 H755 Q802,0 802,48 V68 L792,76 H802 V280"/>
    <path d="M557,76 L567,68"/>
    <!-- bottom dust flaps -->
    <path d="M312,1055 V1067 L325,1077 V1125 Q325,1150 350,1150 H512 Q537,1150 537,1125 V1070 L557,1055"/>
    <path d="M802,1055 L822,1070 V1125 Q822,1150 847,1150 H1010 Q1035,1150 1035,1125 V1077 L1047,1067 V1055"/>
    <!-- bottom tuck lid -->
    <path d="M557,1055 V1259 L567,1267 V1287 Q567,1335 615,1335 H755 Q802,1335 802,1287 V1267 L792,1259 H802 V1055"/>
  </svg>
</main>
</body>
</html>
```